Emerging Ed-Tech Startup seeking Stationery Designs!

We are in need of basic set of stationery designs to be used for our business operations, letters, emails, and in-office materials. We are a technology startup enhancing on campus work experience offerings by establishing a collaborative work environment for the completion of such tasks.

Our colors are Vibrant Tiffany Blue/Black/White.

Website: www.scholarhorizonhub.com (Still under construction aside from the landing pages)

Please make sure the designs use a brighter more vibrant tiffany blue color than seen in the image files uploaded. We are not using those materials.

Our logo has been added as a file as well, please use that for any designs (include that logo). Thank you.

```html
<!DOCTYPE html>
<html lang="en">
<head>
<meta charset="utf-8">
<title>Scholar Horizon Hub — Stationery Set</title>
<link rel="stylesheet" href="https://fonts.googleapis.com/css2?family=Open+Sans:wght@400;600;700&display=swap">
<style>
  :root{
    --tiffany:#3df5d2;
    --ink:#111111;
    --paper:#ffffff;
    --paper-shade:#eef0ef;
    --stage:#e9e6e2;
    --rule:#333333;
    --muted:#555555;
  }
  *{box-sizing:border-box;margin:0;padding:0}
  html,body{width:1200px;height:540px;overflow:hidden}
  body{background:var(--stage);font-family:"Open Sans",Arial,sans-serif;color:var(--ink);position:relative}

  .sheet{position:absolute;background:var(--paper);box-shadow:0 2px 6px rgba(0,0,0,.18);overflow:hidden}
  .brand{position:absolute;display:flex;align-items:center;gap:5px;font-weight:700;color:var(--ink);line-height:1.05;text-transform:uppercase}
  .brand-mark{width:10px;height:10px;background:var(--tiffany);flex:none}
  .brand-name{font-size:11px;letter-spacing:.2px;white-space:nowrap}
  .brand-name span{display:block}

  .contact-list{position:absolute;list-style:none;font-size:5.6px;line-height:8.2px;color:var(--ink);border-left:1px solid var(--ink);padding-left:4px;white-space:nowrap}
  .contact-list li{display:flex;align-items:center;gap:3px}
  .icon{width:6px;height:6px;flex:none}

  .footer-rule{position:absolute;left:0;right:0;height:3px;background:var(--ink)}
  .footer-band{position:absolute;left:0;right:0;bottom:0;background:var(--tiffany);display:flex;align-items:center;color:#fff;font-size:6px;letter-spacing:.6px;white-space:nowrap}

  /* Letterhead */
  .letterhead{left:19px;top:36px;width:338px;height:438px}
  .letterhead .brand{left:13px;top:14px}
  .letterhead .contact-list{right:8px;top:16px;font-size:5.2px;line-height:7.8px}
  .letterhead .footer-rule{bottom:21px}
  .letterhead .footer-band{height:18px;justify-content:center}

  /* Fax */
  .fax{left:404px;top:40px;width:339px;height:438px}
  .fax .brand{left:18px;top:14px}
  .fax-address{position:absolute;left:261px;top:20px;font-size:5.6px;line-height:8px;border-left:1px solid var(--ink);padding-left:4px;white-space:nowrap}
  .fax-title{position:absolute;left:18px;top:92px;font-size:20px;font-weight:400;letter-spacing:.5px}
  .fax-fields{position:absolute;left:18px;top:130px;width:290px;display:grid;grid-template-columns:150px 120px;column-gap:20px;row-gap:6px}
  .fax-field{font-size:5.6px;border-bottom:1px solid var(--rule);padding-bottom:2px;height:12px;display:flex;align-items:flex-end}
  .fax-options{position:absolute;left:18px;top:215px;display:flex;gap:14px;font-size:5.6px;white-space:nowrap}
  .fax-options span{display:flex;align-items:center;gap:3px}
  .checkbox{width:7px;height:7px;border:1px solid var(--rule)}
  .fax .footer-rule{bottom:19px}
  .fax .footer-band{height:17px;justify-content:center;gap:14px;color:var(--ink);font-size:5.4px;letter-spacing:0}
  .fax .footer-band span{display:flex;align-items:center;gap:3px}

  /* Envelopes */
  .envelope{position:absolute;background:var(--paper-shade);box-shadow:0 2px 6px rgba(0,0,0,.18);overflow:hidden}
  .envelope-back{left:798px;top:42px;width:377px;height:243px;background:#f6f6f6}
  .envelope-open{left:786px;top:116px;width:377px;height:236px;background:#f3f3f3}
  .flap{position:absolute;left:0;top:0;width:100%}
  .envelope-front{left:760px;top:201px;width:378px;height:169px;background:linear-gradient(180deg,#fafafa,#ececec)}
  .envelope-front .brand{left:14px;top:12px}
  .envelope-front .footer-rule{bottom:17px}
  .envelope-front .footer-band{height:15px;justify-content:space-between;padding:0 10px;color:var(--ink);font-size:6px}

  /* Business cards */
  .card{position:absolute;width:139px;height:80px;box-shadow:0 2px 5px rgba(0,0,0,.2);overflow:hidden}
  .card-front{left:782px;top:398px;background:var(--paper)}
  .card-front .brand{left:0;right:0;top:8px;justify-content:center;gap:4px}
  .card-front .brand-name{font-size:7px}
  .card-front .brand-mark{width:6px;height:6px}
  .card-person{position:absolute;right:87px;top:48px;text-align:right;font-size:4.6px;line-height:6px;white-space:nowrap}
  .card-person strong{display:block;font-size:5.2px}
  .card-front .contact-list{left:54px;top:43px;font-size:3.6px;line-height:5.6px}
  .card-front .contact-list .icon{width:4px;height:4px}
  .card-front .footer-band{height:7px;justify-content:center;font-size:3.4px;letter-spacing:.3px}
  .card-back{left:933px;top:399px;background:var(--tiffany);color:#fff}
  .card-back .brand{left:0;right:0;top:20px;justify-content:center;color:#fff}
  .card-back .brand-mark{background:#fff}
  .card-back .brand-name{font-size:9.5px}
  .card-back-url{position:absolute;left:0;right:0;top:61px;text-align:center;font-size:5.6px;color:var(--ink)}

  .option-label{position:absolute;top:494px;font-size:20px;color:#333}
</style>
</head>
<body>

<svg width="0" height="0" style="position:absolute" aria-hidden="true">
  <defs>
    <symbol id="i-phone" viewBox="0 0 10 10"><circle cx="5" cy="5" r="4.4" fill="none" stroke="currentColor" stroke-width="1"/><path d="M3.3 2.8l1 0 .4 1.2-.6.5a3 3 0 0 0 1.4 1.4l.5-.6 1.2.4v1a.7.7 0 0 1-.8.6A4.3 4.3 0 0 1 2.7 3.6a.7.7 0 0 1 .6-.8z" fill="currentColor"/></symbol>
    <symbol id="i-mail" viewBox="0 0 10 10"><rect x="1" y="2.5" width="8" height="5" fill="currentColor"/></symbol>
    <symbol id="i-web" viewBox="0 0 10 10"><circle cx="5" cy="5" r="4" fill="currentColor"/><path d="M1 5h8M5 1v8" stroke="#fff" stroke-width=".6"/></symbol>
  </defs>
</svg>

<!-- Letterhead -->
<section class="sheet letterhead" aria-label="Letterhead">
  <div class="brand"><span class="brand-mark"></span><span class="brand-name"><span>Scholar Horizon</span><span>Hub</span></span></div>
  <ul class="contact-list">
    <li><svg class="icon"><use href="#i-phone"/></svg>+91 20 4455120</li>
    <li><svg class="icon"><use href="#i-phone"/></svg>+91 20 4455137</li>
    <li><svg class="icon"><use href="#i-mail"/></svg>hello@scholarhorizonhub.com</li>
    <li><svg class="icon"><use href="#i-web"/></svg>www.scholarhorizonhub.com</li>
  </ul>
  <div class="footer-rule"></div>
  <div class="footer-band">Street Name, City Name State Zipcode</div>
</section>

<!-- Fax cover -->
<section class="sheet fax" aria-label="Fax cover sheet">
  <div class="brand"><span class="brand-mark"></span><span class="brand-name"><span>Scholar Horizon</span><span>Hub</span></span></div>
  <p class="fax-address">Street Name, City Name<br>State Zipcode</p>
  <h1 class="fax-title">FAX</h1>
  <div class="fax-fields">
    <div class="fax-field">To :</div><div class="fax-field">From :</div>
    <div class="fax-field">Fax :</div><div class="fax-field">Pages :</div>
    <div class="fax-field">Phone :</div><div class="fax-field">Date :</div>
    <div class="fax-field">Re :</div><div class="fax-field">CC :</div>
  </div>
  <div class="fax-options">
    <span><i class="checkbox"></i>Urgent</span>
    <span><i class="checkbox"></i>For Review</span>
    <span><i class="checkbox"></i>Please Comment</span>
    <span><i class="checkbox"></i>Please Reply</span>
    <span><i class="checkbox"></i>Please Recycle</span>
  </div>
  <div class="footer-rule"></div>
  <div class="footer-band">
    <span><svg class="icon"><use href="#i-phone"/></svg>+91 20 4455120</span>
    <span><svg class="icon"><use href="#i-phone"/></svg>+91 20 4455137</span>
    <span><svg class="icon"><use href="#i-mail"/></svg>hello@scholarhorizonhub.com</span>
    <span><svg class="icon"><use href="#i-web"/></svg>www.scholarhorizonhub.com</span>
  </div>
</section>

<!-- Envelopes -->
<div class="envelope envelope-back" aria-label="Envelope back, black flap">
  <svg class="flap" viewBox="0 0 377 90" height="90" preserveAspectRatio="none"><path d="M0 0H377L360 50Q355 58 345 60L200 86Q188 88 176 86L32 60Q22 58 17 50Z" fill="var(--ink)"/></svg>
</div>
<div class="envelope envelope-open" aria-label="Envelope back, tiffany flap">
  <svg class="flap" viewBox="0 0 377 90" height="90" preserveAspectRatio="none"><path d="M0 0H377L360 50Q355 58 345 60L200 86Q188 88 176 86L32 60Q22 58 17 50Z" fill="var(--tiffany)"/></svg>
</div>
<section class="envelope envelope-front" aria-label="Envelope front">
  <div class="brand"><span class="brand-mark"></span><span class="brand-name"><span>Scholar Horizon</span><span>Hub</span></span></div>
  <div class="footer-rule"></div>
  <div class="footer-band"><span>Street Name, City Name State Zipcode</span><span>www.scholarhorizonhub.com</span></div>
</section>

<!-- Business cards -->
<section class="card card-front" aria-label="Business card front">
  <div class="brand"><span class="brand-mark"></span><span class="brand-name"><span>Scholar Horizon</span><span>Hub</span></span></div>
  <p class="card-person"><strong>Your Name</strong>Title</p>
  <ul class="contact-list">
    <li><svg class="icon"><use href="#i-phone"/></svg>+91 20 4455120</li>
    <li><svg class="icon"><use href="#i-phone"/></svg>+91 20 4455137</li>
    <li><svg class="icon"><use href="#i-mail"/></svg>hello@scholarhorizonhub.com</li>
    <li><svg class="icon"><use href="#i-web"/></svg>www.scholarhorizonhub.com</li>
  </ul>
  <div class="footer-band">Street Name, City Name State Zipcode</div>
</section>
<section class="card card-back" aria-label="Business card back">
  <div class="brand"><span class="brand-mark"></span><span class="brand-name"><span>Scholar Horizon</span><span>Hub</span></span></div>
  <p class="card-back-url">www.scholarhorizonhub.com</p>
</section>

<p class="option-label" style="left:128px">Option-1</p>
<p class="option-label" style="left:535px">Option-2</p>

</body>
</html>
```